Design + Finalize Lead Magnet

Lead Magnet:
"7 Hidden Payroll Traps Builders Miss — Plus Simple Ways to Fix Each One"
Create a polished, professional PDF lead magnet based on provided content. This guide will be offered as a downloadable resource to construction contractors via LinkedIn, email, and our website. The purpose is to build trust, demonstrate expertise in workers’ compensation insurance, and generate qualified leads for Brelvon
Insurance.
Project Scope:
Design the Lead Magnet (8–10 pages):
Use the full text provided in the document.
Include a visually engaging cover page (title, logo, clean construction image).
Use section headers, checklists, icons, and callouts for easier reading.
Incorporate the MOD Rate Improvement Checklist as a visual checklist (bullets or checkboxes).
Create a strong call to action page at the end with contact info and a link to request a free Workers’ Comp Risk Assessment.

Style Requirements:
Professional and clean design suited to construction contractors
Use brand colors: navy, gray, white, and accent blue/teal
Fonts: Montserrat, Lato, or Open Sans (modern, easy to read)
Include space for our logo and contact info in footer or closing page

Export & Delivery:
Final product as a high-resolution PDF (optimized for web/email)
Optional: Separate Canva template link for future edits

```html
<!DOCTYPE html>
<html lang="en">
<head>
<meta charset="UTF-8">
<title>Brelvon Lead Magnet – Page Spreads</title>
<link rel="stylesheet" href="https://fonts.googleapis.com/css2?family=Poppins:ital,wght@0,400;0,500;0,600;1,400&display=swap">
<style>
:root{
  --navy:#22205e;
  --charcoal:#353535;
  --ink:#222;
  --teal:#2f8a8c;
  --blue:#1f6fc6;
  --mist:#f1f1f3;
  --white:#fff;
  --rule:#555;
}
*{margin:0;padding:0;box-sizing:border-box}
html,body{width:1200px;height:3000px;overflow:hidden;background:var(--white);font-family:"Poppins",sans-serif;color:var(--ink)}
.page{position:absolute;left:256px;width:688px;height:891px;background:var(--white);overflow:hidden;box-shadow:0 6px 22px rgba(0,0,0,.22)}
.page--cover{top:97px}
.page--intro{top:1054px}
.page--mistakes{top:2013px}

/* cover */
.cover__brand{position:absolute;left:62px;top:118px;display:flex;align-items:center;gap:10px;font-weight:500;font-size:26px;color:var(--ink)}
.cover__brand-dot{width:22px;height:22px;border-radius:50%;background:var(--navy)}
.cover__panel{position:absolute;left:0;top:242px;width:383px;height:590px}
.cover__photo{position:absolute;left:340px;top:0;width:348px;height:801px;background:linear-gradient(180deg,#f6df98 0%,#f3c777 45%,#d08a4c 75%,#4a3c38 100%)}
.cover__title{position:absolute;left:60px;top:308px;width:265px;color:var(--white);font-size:30px;font-weight:500;line-height:37px}
.cover__subtitle{position:absolute;left:60px;top:578px;width:200px;color:var(--white);font-size:15px;line-height:19px}
.cover__rule{position:absolute;left:60px;top:727px;width:72px;height:1px;background:var(--white)}
.cover__author{position:absolute;left:60px;top:750px;color:var(--white);font-size:8.5px;line-height:10.5px}
.cover__author strong{font-weight:600}
.cover__author em{font-style:italic}
.cover__url{position:absolute;left:398px;top:813px;font-size:16px;letter-spacing:1.2px;color:var(--ink)}

/* intro */
.intro__photo{position:absolute;left:0;top:0;width:449px;height:803px;background:linear-gradient(160deg,#4c6e74 0%,#9aa7a6 35%,#c98a3e 55%,#5b4b3f 80%,#7c8a8a 100%)}
.intro__box{position:absolute;left:241px;top:148px;width:371px;height:572px;background:rgba(53,53,53,.97);color:var(--white);padding:34px 36px}
.intro__heading{font-size:41px;font-weight:500;line-height:48px;margin-bottom:42px}
.intro__body p{font-size:14.5px;line-height:17.6px;margin-bottom:17px}
.intro__rule{position:absolute;left:47px;top:832px;width:584px;height:1px;background:var(--rule)}

/* mistakes */
.mistakes__photo-top{position:absolute;left:0;top:0;width:264px;height:487px;background:linear-gradient(170deg,#53554f 0%,#8a8a84 45%,#c4b56a 70%,#3e3e3c 100%)}
.mistakes__photo-bottom{position:absolute;left:0;top:487px;width:264px;height:404px;background:linear-gradient(170deg,#4b4f57 0%,#8c8f6a 40%,#c9d04a 60%,#3c3f45 100%)}
.mistakes__strip{position:absolute;left:41px;top:0;width:223px;height:891px;background:rgba(30,32,36,.72)}
.mistakes__band{position:absolute;left:264px;top:487px;width:424px;height:404px;background:var(--mist)}
.mistake__label{position:absolute;left:61px;display:flex;align-items:center;gap:11px;color:var(--white);font-size:27px;font-weight:500}
.mistake__num{width:47px;height:47px;border-radius:50%;background:var(--blue);display:flex;align-items:center;justify-content:center;font-size:24px}
.mistake__name{position:absolute;left:61px;width:190px;color:var(--white);font-size:22px;font-weight:500;line-height:25.5px}
.mistake__copy{position:absolute;left:294px;width:340px;font-size:13px;line-height:16px}
.mistake__copy h3{font-size:13px;font-weight:600;color:var(--teal);line-height:16px}
.mistake__copy p{margin-bottom:23px}
</style>
</head>
<body>

<section class="page page--cover">
  <div class="cover__brand"><span class="cover__brand-dot"></span>Brelvon</div>
  <div class="cover__photo" role="img" aria-label="Construction site at sunset with tower crane, building frame and silhouetted workers"></div>
  <svg class="cover__panel" viewBox="0 0 383 590" aria-hidden="true"><polygon points="0,0 340,0 340,559 383,559 363,590 0,590" fill="#22205e"/></svg>
  <h1 class="cover__title">7 Hidden Payroll Traps Builders Miss — Plus Simple Ways to Fix Each One</h1>
  <p class="cover__subtitle">A Practical Guide for Construction Business Owners</p>
  <div class="cover__rule"></div>
  <p class="cover__author"><strong>Marisol Vantero</strong><br><em>Licensed Agent/Broker<br>at Brelvon Insurance &amp; Consulting<br>Workers’ Compensation Specialists</em></p>
  <p class="cover__url">brelvoninsurance.com</p>
</section>

<section class="page page--intro">
  <div class="intro__photo" role="img" aria-label="Orange excavator on a muddy construction site in front of a blurred building"></div>
  <div class="intro__box">
    <h2 class="intro__heading">Why This<br>Guide Matters</h2>
    <div class="intro__body">
      <p>As a contractor, your time, money, and reputation are on the line. Workers’ compensation costs can skyrocket due to preventable mistakes—hurting your business and your bottom line.</p>
      <p>Workers’ compensation can be one of the most expensive and misunderstood areas of business for contractors. One mistake—like misclassifying employees or skipping safety training—can lead to huge premium increases or denied claims.</p>
      <p>This guide highlights the top errors contractors make and provides straightforward solutions to help you stay compliant, reduce risk, and protect your workforce.</p>
    </div>
  </div>
  <div class="intro__rule"></div>
</section>

<section class="page page--mistakes">
  <div class="mistakes__photo-top" role="img" aria-label="Gloved hands reviewing construction blueprints"></div>
  <div class="mistakes__photo-bottom" role="img" aria-label="Worker in hard hat and high-visibility vest seen from above"></div>
  <div class="mistakes__strip"></div>
  <div class="mistakes__band"></div>

  <div class="mistake__label" style="top:68px">Mistake <span class="mistake__num">1</span></div>
  <h2 class="mistake__name" style="top:164px">Misclassifying Employees</h2>
  <div class="mistake__copy" style="top:78px">
    <h3>Why it matters:</h3>
    <p>Misclassifying workers incorrectly is one of the most common-and expensive-mistakes contractors make. Whether it’s assigning clerical codes to field workers or lumping all employees into a single category, misclassification can result in denied claims, audit penalties, backdated premium increases, or even regulatory fines. Insurance carriers determine your workers’ comp rates based on the risk level associated with each job duty, so accuracy matters.</p>
    <h3>Avoid it:</h3>
    <p>Conduct regular reviews of employee job duties with your insurance broker, especially when roles change or new services are added. Make sure you’re using the correct class codes as defined by your state’s rating bureau or NRCB. When in doubt, ask your broker to help you confirm classifications before a policy is issued—or audited.</p>
  </div>

  <div class="mistake__label" style="top:550px">Mistake <span class="mistake__num">2</span></div>
  <h2 class="mistake__name" style="top:636px">Not Collecting Certificates of Insurance (COIs) from Subcontractors</h2>
  <div class="mistake__copy" style="top:556px">
    <h3>Why it matters:</h3>
    <p>If a subcontractor doesn’t have their own active workers’ comp policy, your business could be held liable for their injuries. This often results in surprise audit charges or even denied claims. Not collecting COIs can inflate your payroll exposure and raise red flags during audits.</p>
    <h3>Avoid it:</h3>
    <p>Always request and verify up-to-date COIs for every subcontractor before they step on site. Keep copies of COIs for your records and set calendar reminders to follow up on expirations. Your insurance broker can also help you implement a subcontractor tracking system.</p>
  </div>
</section>

</body>
</html>
```